Business Card Design Project

We require a professional business card designed for our consulting organisation that has the same theme and colours as our logo except for the grey.

Colours on the front should predominately be white however some reference to our logo colours except for the grey.

The back of the card should be have background colour that aligns with our logo colour.

Layout, style and design is up to the designer. So send through your designs

Details are attached in the word document project brief.

Target Market(s)

Target market are large corporate organisations

Industry/Entity Type

Business

Requirements
Must have
• Content on the front must have:

Dean Halvorsen
Managing Director

P: 0417 285 394
E: Dean@brevolinkpartners.com
W: www.brevolinkpartners.com

Content on the back must have the words:
Alliances
Placement
Training
Support

Design Colours
Must align to our logo

```html
<!DOCTYPE html>
<html lang="en">
<head>
<meta charset="utf-8">
<title>BrevoLink Partners – Business Cards</title>
<link rel="stylesheet" href="https://fonts.googleapis.com/css2?family=Open+Sans:wght@400;600;700&display=swap">
<style>
  :root {
    --brand-blue: #1b75bc;
    --brand-blue-light: #2b8fd6;
    --brand-grey: #58595b;
    --text-dark: #3a3a3c;
    --card-white: #ffffff;
    --backdrop: #e7e8ea;
    --divider: #c4c6c9;
  }
  * { box-sizing: border-box; margin: 0; padding: 0; }
  html, body {
    width: 1200px; height: 720px; overflow: hidden;
    background: var(--backdrop);
    font-family: "Open Sans", Arial, sans-serif;
  }
  .stage { position: relative; width: 1200px; height: 720px; }

  .card {
    position: absolute;
    width: 540px; height: 300px;
    background: var(--card-white);
    box-shadow: 0 6px 18px rgba(0,0,0,0.14);
    overflow: hidden;
  }
  .card--front { left: 40px; top: 110px; }
  .card--back  { left: 620px; top: 310px; }

  .card__swoosh { position: absolute; inset: 0; width: 100%; height: 100%; }

  .brand {
    position: absolute;
    display: flex; align-items: center; gap: 14px;
  }
  .brand__mark {
    width: 20px; height: 20px; border-radius: 50%;
    background: var(--brand-blue);
    flex: none;
  }
  .brand__name {
    font-weight: 700;
    color: var(--brand-blue);
    line-height: 1.05;
    letter-spacing: 0.5px;
  }
  .card--front .brand { left: 34px; top: 70px; }
  .card--front .brand__name { font-size: 27px; }
  .card--back .brand { left: 78px; top: 66px; }
  .card--back .brand__mark { width: 28px; height: 28px; }
  .card--back .brand__name { font-size: 36px; }

  .holder { position: absolute; left: 34px; top: 200px; }
  .holder__name { font-size: 17px; font-weight: 700; color: var(--brand-blue); }
  .holder__title { font-size: 13px; color: var(--text-dark); margin-top: 1px; }

  .contact {
    position: absolute; right: 22px; top: 44px;
    list-style: none; text-align: right;
    color: var(--card-white); font-size: 12.5px;
  }
  .contact__item {
    display: flex; align-items: center; justify-content: flex-end;
    gap: 7px; margin-bottom: 8px;
  }
  .contact__item--phone { margin-bottom: 26px; }
  .contact__icon { width: 13px; height: 13px; flex: none; }

  .services {
    position: absolute; left: 150px; top: 160px;
    display: flex; align-items: stretch;
    font-size: 21px; color: var(--text-dark); line-height: 1.15;
  }
  .services__col { padding: 0 14px; }
  .services__col--left { text-align: right; }
  .services__divider { width: 1px; background: var(--divider); }

  .website {
    position: absolute; left: 0; right: 0; bottom: 22px;
    text-align: center; font-size: 15px; letter-spacing: 1px;
    color: var(--text-dark);
  }
  .website__accent { color: var(--brand-blue); font-weight: 600; }
</style>
</head>
<body>
<main class="stage">

  <section class="card card--front" aria-label="Business card front">
    <svg class="card__swoosh" viewBox="0 0 540 300" preserveAspectRatio="none" aria-hidden="true">
      <path d="M295,0 C280,140 230,240 150,300 L180,300 C260,240 330,140 360,0 Z" fill="var(--brand-grey)"/>
      <path d="M360,0 C330,140 260,240 180,300 L540,300 L540,0 Z" fill="var(--brand-blue)"/>
    </svg>

    <div class="brand">
      <span class="brand__mark"></span>
      <span class="brand__name">BrevoLink<br>Partners</span>
    </div>

    <div class="holder">
      <p class="holder__name">Dean Halvorsen</p>
      <p class="holder__title">Managing Director</p>
    </div>

    <ul class="contact">
      <li class="contact__item contact__item--phone">
        <svg class="contact__icon" viewBox="0 0 16 16" aria-hidden="true">
          <circle cx="8" cy="8" r="7.3" fill="none" stroke="#fff" stroke-width="1.2"/>
          <path d="M5.3 4.2l1.4-.3.8 2-1 .7a5 5 0 0 0 2.4 2.4l.7-1 2 .8-.3 1.4c-3.2.3-6.3-2.8-6-6z" fill="#fff"/>
        </svg>
        <span>P: 0417 285 394</span>
      </li>
      <li class="contact__item">
        <svg class="contact__icon" viewBox="0 0 16 16" aria-hidden="true">
          <rect x="1.5" y="3.5" width="13" height="9" fill="none" stroke="#fff" stroke-width="1.3"/>
          <path d="M1.5 3.5L8 9l6.5-5.5" fill="none" stroke="#fff" stroke-width="1.3"/>
        </svg>
        <span>E: Dean@brevolinkpartners.com</span>
      </li>
      <li class="contact__item">
        <svg class="contact__icon" viewBox="0 0 16 16" aria-hidden="true">
          <circle cx="8" cy="8" r="6.5" fill="none" stroke="#fff" stroke-width="1.2"/>
          <ellipse cx="8" cy="8" rx="3" ry="6.5" fill="none" stroke="#fff" stroke-width="1"/>
          <path d="M1.5 8h13M2.5 5h11M2.5 11h11" stroke="#fff" stroke-width="0.9"/>
        </svg>
        <span>W: www.brevolinkpartners.com</span>
      </li>
    </ul>
  </section>

  <section class="card card--back" aria-label="Business card back">
    <div class="brand">
      <span class="brand__mark"></span>
      <span class="brand__name">BrevoLink<br>Partners</span>
    </div>

    <div class="services">
      <div class="services__col services__col--left">
        <p>Alliances</p>
        <p>Placement</p>
      </div>
      <span class="services__divider"></span>
      <div class="services__col">
        <p>Training</p>
        <p>Support</p>
      </div>
    </div>

    <p class="website">www.<span class="website__accent">brevolink</span>partners.com</p>
  </section>

</main>
</body>
</html>
```